Redesign the Eshop of a gift shop

We want to redesign the front page, the category page and the product page of our Eshop that sells gifts.
I am thinking not to reveal the url of the eshop as i don't want you to get influenced. Lets call the Eshop "PresentNook.com"
I will list the brands that we resell so you understand what we are selling,
Vorelli-https://www.vorelli-example.com/
Brimworth-https://brimworth-example.com/
Pandol - https://pandol-example.com/
Quiet Meadow - https://www.quietmeadow-example.com/
Fellow's Toolchest - https://fellowstoolchest-example.com/
Paperloft ink - https://paperloftink-example.com/
Pretzel - https://pretzelofficial-example.com/
We also sell toys for adults like backgamon, chess, playing cards, board games.
The problem is that many eshops sell these and thats why i would like the design to have a different approach, more fresh, not seen before.
I am also thinking of something playfull, happy, but warm at the same time.
Please note that our logo is black & white but feel free to play with any color/s you like in your website design. We might eventually even adjust the logo colors, or you can provide a pallete that suites a black and white logo
Let me know if you have any questions!
Target Market(s)
Age: 20-50, Gender: Also men but mostly women, Income: Moderate to high, Interests and Lifestyle: Customers who value sentimentality, personal connection, and thoughtful gestures, Relationship Status: Those in relationships or with larger families
Number of Pages Required
3 page
Look and feel
Each slider illustrates characteristics of the customer's brand and the style your logo design should communicate.

```html
<!DOCTYPE html>
<html lang="en">
<head>
<meta charset="utf-8">
<title>PresentNook.com — Premium Collection</title>
<link href="https://fonts.googleapis.com/css2?family=Poppins:wght@300;400;500;600;700;900&display=swap" rel="stylesheet">
<style>
  :root {
    --ink: #111111;
    --muted: #555555;
    --nav: #444444;
    --hero-bg: #e6e6e6;
    --page-bg: #ffffff;
    --accent: #e8322f;
    --white: #ffffff;
  }
  * { box-sizing: border-box; margin: 0; padding: 0; }
  html, body {
    width: 1200px; height: 696px; overflow: hidden;
    background: var(--page-bg);
    font-family: "Poppins", sans-serif;
    color: var(--ink);
  }
  .page { position: relative; width: 1200px; height: 696px; }

  .site-header { position: absolute; top: 0; left: 0; width: 1200px; height: 76px; }
  .brand {
    position: absolute; left: 57px; top: 28px;
    display: flex; align-items: center; gap: 7px;
    font-size: 17px; font-weight: 400; letter-spacing: 1px; color: var(--ink);
  }
  .brand-mark { width: 12px; height: 12px; background: var(--ink); }
  .main-nav { position: absolute; top: 33px; left: 0; }
  .main-nav a {
    position: absolute; white-space: nowrap;
    font-size: 11px; font-weight: 400; letter-spacing: 0.4px;
    color: var(--nav); text-decoration: none;
  }
  .main-nav a.is-active { color: var(--ink); font-weight: 500; }
  .header-icons svg { position: absolute; top: 31px; }

  .hero { position: absolute; left: 0; top: 76px; width: 1200px; height: 545px; background: var(--hero-bg); }
  .hero-kicker { position: absolute; left: 122px; top: 134px; font-size: 16px; font-weight: 600; letter-spacing: -0.4px; }
  .hero-title { position: absolute; left: 118px; top: 148px; font-size: 60px; font-weight: 700; letter-spacing: -2px; line-height: 1.2; }
  .hero-art { position: absolute; left: 0; top: 0; }
  .cta {
    position: absolute; left: 116px; top: 367px; width: 158px; height: 38px;
    border-radius: 19px; background: var(--accent); color: var(--white);
    font-size: 11.5px; font-weight: 400; letter-spacing: 0.3px;
    display: flex; align-items: center; justify-content: center; text-decoration: none;
  }
  .description { position: absolute; right: 104px; top: 370px; text-align: right; }
  .description h2 { font-size: 12px; font-weight: 600; letter-spacing: -0.3px; margin-bottom: 7px; }
  .description p { font-size: 9.5px; font-weight: 300; line-height: 13.5px; color: var(--muted); letter-spacing: 0.3px; }
</style>
</head>
<body>
<div class="page">
  <header class="site-header">
    <div class="brand"><span class="brand-mark"></span>PRESENTNOOK</div>
    <nav class="main-nav">
      <a class="is-active" href="#" style="left:748px">New</a>
      <a href="#" style="left:810px">Shop</a>
      <a href="#" style="left:877px">Sale</a>
      <a href="#" style="left:940px">Pack Your Dream</a>
    </nav>
    <div class="header-icons">
      <svg style="left:1094px" width="17" height="17" viewBox="0 0 17 17" fill="none" stroke="#222" stroke-width="1.3" aria-label="Search">
        <circle cx="7" cy="7" r="5.8"/><line x1="11.2" y1="11.2" x2="16" y2="16"/>
      </svg>
      <svg style="left:1133px" width="17" height="17" viewBox="0 0 17 17" fill="none" stroke="#222" stroke-width="1.2" aria-label="Basket">
        <path d="M4.5 6 A4 4 0 0 1 12.5 6"/>
        <path d="M1.5 6.5 H15.5 L14 15.5 H3 Z"/>
        <line x1="6.5" y1="9" x2="6.5" y2="13"/><line x1="8.5" y1="9" x2="8.5" y2="13"/><line x1="10.5" y1="9" x2="10.5" y2="13"/>
      </svg>
    </div>
  </header>

  <section class="hero">
    <svg class="hero-art" width="1200" height="545" viewBox="0 0 1200 545">
      <defs>
        <linearGradient id="productTones" x1="0" y1="0" x2="1" y2="1">
          <stop offset="0%" stop-color="#b98a63"/>
          <stop offset="40%" stop-color="#9a6a45"/>
          <stop offset="75%" stop-color="#c7a47f"/>
          <stop offset="100%" stop-color="#b89476"/>
        </linearGradient>
        <radialGradient id="floorShadow" cx="50%" cy="50%" r="50%">
          <stop offset="0%" stop-color="#9a9a9a" stop-opacity="0.55"/>
          <stop offset="100%" stop-color="#e6e6e6" stop-opacity="0"/>
        </radialGradient>
      </defs>
      <text x="110" y="344" font-family="Poppins, sans-serif" font-weight="900" font-size="165" textLength="985" lengthAdjust="spacingAndGlyphs" fill="#ffffff">COLLECTION</text>
      <ellipse cx="680" cy="450" rx="300" ry="26" fill="url(#floorShadow)"/>
      <rect x="458" y="70" width="438" height="378" rx="42" fill="url(#productTones)" role="img" aria-label="Product photo: leather wallet, woven basket with flowers, pen and canvas backpack"/>
      <text x="110" y="344" font-family="Poppins, sans-serif" font-weight="900" font-size="165" textLength="985" lengthAdjust="spacingAndGlyphs" fill="none" stroke="#ffffff" stroke-width="1">COLLECTION</text>
    </svg>
    <p class="hero-kicker">Slected Items</p>
    <h1 class="hero-title">Premium</h1>
    <a class="cta" href="#">Shop By Category</a>
    <div class="description">
      <h2>Description</h2>
      <p>Lorem ipsum dolor sit amet,<br>consectetur adipiscing elit, sed<br>do eiusmod tempor</p>
    </div>
  </section>
</div>
</body>
</html>
```